Wine Tasting Event

We need a flyer design for a wine tasting event on Friday, February 14th. This is NOT a Valentine's themed event. It's merely an event for both singles and couples who do not want to drop a ton of money on a traditional meal at a fine restaurant. There will be good wines to taste, light snacks, info sessions on how to taste/appreciate good wine, live music, and a full bar in addition to the wine.

The event is called "Poured on the Millrace" and will be held at a venue overlooking the beautiful Harwick Greenway path.

We had an initial idea of a Large Wine cork taking up the majority of the flyer, with all of the information printed on it (as if it were a part of the cork). We are not designers, but have attached the initial attempt at the idea. Warning - It's bad.

Target Market(s)

Men and Women aged 21-35.

Industry/Entity Type

Restaurant

Requirements
Must have
• Name: Poured on the Millrace
Date: Friday, February 14th
Logo: Dunmore Play and Mixer League (See Attached File)

*NOTE Logo should not be a focal point of design. Just needs to be somewhere on the flyer. Can be substituted fo "Dunmore Play and Mixer League Presents"

Needs to be adaptable for 4"x6", 8.5"x11", and 11"x17"
Nice to have
• Wine cork, bottle, or glass. Something Atlanta related, or related to the Harwick Greenway.
Should not have
• Anything related to Valentine's Day

```html
<!DOCTYPE html>
<html lang="en">
<head>
<meta charset="utf-8">
<title>Poured on the Millrace — Flyer</title>
<link rel="stylesheet" href="https://fonts.googleapis.com/css2?family=Pinyon+Script&family=PT+Sans:wght@400&family=Roboto+Condensed:wght@300;400&display=swap">
<style>
  :root {
    --ink: #0a0a0b;
    --flyer: #0c0c0d;
    --glow: #b3120a;
    --orange: #f08a1c;
    --white: #ffffff;
    --wine-deep: #1c0805;
    --wine-red: #5a140c;
    --wine-amber: #9a4a18;
    --bokeh-warm: #c8502a;
    --park-sky: #2f4a86;
    --park-haze: #5d6a8a;
    --park-lamp: #c9a84a;
    --park-green: #4f7a2c;
  }
  * { margin: 0; padding: 0; box-sizing: border-box; }
  html, body { width: 1000px; height: 1200px; overflow: hidden; background: var(--ink); }
  .canvas {
    position: relative; width: 1000px; height: 1200px; overflow: hidden;
    background:
      radial-gradient(ellipse 200px 430px at 40px 470px, rgba(179,18,10,0.95), rgba(179,18,10,0) 100%),
      radial-gradient(ellipse 200px 430px at 960px 470px, rgba(179,18,10,0.95), rgba(179,18,10,0) 100%),
      var(--ink);
  }
  .flyer {
    position: absolute; left: 200px; top: 122px; width: 628px; height: 948px;
    background: var(--flyer); overflow: hidden;
  }
  .hero-photo {
    position: absolute; left: 0; top: 0; width: 628px; height: 470px;
    background:
      radial-gradient(ellipse 260px 220px at 310px 200px, rgba(154,74,24,0.55), rgba(154,74,24,0) 100%),
      radial-gradient(ellipse 200px 260px at 560px 200px, rgba(200,80,42,0.45), rgba(200,80,42,0) 100%),
      linear-gradient(180deg, var(--wine-red) 0%, var(--wine-deep) 55%, var(--flyer) 100%);
  }
  .headline { font-weight: 400; }
  .title-script {
    position: absolute; left: 0; width: 628px; top: 292px; text-align: center;
    font-family: "Pinyon Script", cursive; font-weight: 400; font-size: 132px; line-height: 1;
    color: var(--white);
  }
  .title-small {
    position: absolute; left: 0; width: 628px; top: 447px; text-align: center;
    font-family: "PT Sans", sans-serif; font-weight: 400; font-size: 22px; letter-spacing: 5px;
    color: var(--orange);
  }
  .title-large {
    position: absolute; left: 0; width: 628px; top: 468px; text-align: center;
    font-family: "PT Sans", sans-serif; font-weight: 400; font-size: 84px; line-height: 1; letter-spacing: 1px;
    color: var(--orange);
  }
  .flourish {
    position: absolute; left: 290px; top: 561px; width: 58px; height: 10px;
    background: linear-gradient(90deg, rgba(240,138,28,0), var(--orange) 30%, var(--orange) 70%, rgba(240,138,28,0));
    opacity: 0.55; border-radius: 5px;
  }
  .date {
    position: absolute; left: 0; width: 628px; top: 582px; text-align: center;
    font-family: "Roboto Condensed", sans-serif; font-weight: 300; font-size: 29px;
    color: var(--white);
  }
  .venue-photo {
    position: absolute; left: 18px; top: 628px; width: 610px; height: 190px;
    background:
      linear-gradient(180deg, var(--flyer) 0%, var(--park-sky) 18%, var(--park-haze) 32%, var(--park-lamp) 44%, var(--park-green) 66%, #22301a 84%, var(--flyer) 100%);
  }
  .presenter {
    position: absolute; left: 0; width: 628px; top: 836px; text-align: center;
    font-family: "Roboto Condensed", sans-serif; font-weight: 400; font-size: 20px;
    color: var(--white);
  }
</style>
</head>
<body>
<main class="canvas">
  <article class="flyer">
    <div class="hero-photo" role="img" aria-label="Photo of two glasses of red wine against blurred colourful lights"></div>
    <h1 class="headline">
      <span class="title-script">Poured</span>
      <span class="title-small">ON THE</span>
      <span class="title-large">MILLRACE</span>
    </h1>
    <div class="flourish" role="img" aria-label="Small decorative scroll ornament"></div>
    <p class="date">Friday, February 14th</p>
    <div class="venue-photo" role="img" aria-label="Night photo of the Harwick Greenway park with lit paths, trees and city buildings"></div>
    <p class="presenter">Dunmore Play and Mixer League</p>
  </article>
</main>
</body>
</html>
```